Business Cards and label design needed!

I am a metalsmith, working in sterling silver, brass and moving slowly into adding some gold accent pieces. I also use patinas to add color to brass pieces. The peacock feather is used in my packaging, as both a label and tissue paper. I am attaching what I am currently using, and printing at home, but I need a design that I can have professionally printed. My website is www.willowharborcrafts.com
Target Market(s)
Established Professionals, Independent thinkers, Art donors, Artist supporters
Industry/Entity Type
Jewelry
Contact Information for Business Card
I would like a business card with the basic contact information, including Facebook and Instagram. I currently use a peacock feather and would like to continue that. I like to use turquoise, Tiffany blue and colors in that direction. I am open to other suggestions. I would like to be able to transfer the design to oval labels as well.
Font styles to use
Other font styles liked:
- Garamond or other fonts that have a slight script that is easy to read
Look and feel

```html
<!DOCTYPE html>
<html lang="en">
<head>
<meta charset="utf-8">
<title>Willow Harbor Crafts – Business Card</title>
<link rel="stylesheet" href="https://fonts.googleapis.com/css2?family=Work+Sans:wght@300;400;500&display=swap">
<style>
  :root {
    --indigo: #27318f;
    --indigo-deep: #232c86;
    --indigo-light: #2f3a9e;
    --teal: #15958d;
    --feather: #2aa6a0;
    --rule: #5c61b0;
    --logo-grey: #7a7d8c;
    --back-text: #d9dcef;
    --stage: #e7e8ee;
  }
  * { margin: 0; padding: 0; box-sizing: border-box; }
  html, body { width: 1200px; height: 900px; overflow: hidden; }
  body {
    background: var(--stage);
    font-family: "Work Sans", Arial, sans-serif;
    display: flex; flex-direction: column; align-items: center; justify-content: center;
    gap: 30px;
  }
  .card {
    position: relative;
    width: 700px; height: 400px;
    box-shadow: 0 8px 24px rgba(20, 24, 60, 0.2);
    overflow: hidden;
  }

  /* Front */
  .card-front {
    background: radial-gradient(ellipse at 65% 35%, #ffffff 0%, #f6f6f8 70%, #ececf0 100%);
  }
  .brand {
    position: absolute; left: 77px; top: 84px;
    display: flex; align-items: center; gap: 12px;
  }
  .brand-dot { width: 15px; height: 15px; border-radius: 50%; background: var(--teal); }
  .brand-name { font-size: 28px; font-weight: 400; letter-spacing: 0.5px; color: var(--logo-grey); }
  .divider {
    position: absolute; left: 49px; top: 231px;
    width: 553px; height: 1.5px; background: var(--rule);
  }
  .person { position: absolute; right: 98px; top: 180px; text-align: right; }
  .person-name {
    font-size: 24px; font-weight: 500; color: var(--indigo);
    letter-spacing: 0.4px; text-transform: uppercase; line-height: 1.1;
  }
  .person-role { font-size: 15px; color: var(--teal); margin-top: 2px; }
  .contact-list { position: absolute; left: 28px; top: 246px; list-style: none; }
  .contact-list li {
    display: flex; align-items: center; gap: 9px;
    font-size: 16px; color: var(--teal); line-height: 24px;
  }
  .contact-list svg { width: 11px; height: 11px; flex: none; }
  .address { position: absolute; right: 77px; top: 334px; font-size: 17px; color: var(--teal); }
  .base-band {
    position: absolute; left: 0; right: 0; bottom: 0; height: 11px;
    display: flex; gap: 6px;
  }
  .band-indigo { width: 252px; background: var(--indigo); }
  .band-teal { flex: 1; background: var(--teal); }

  /* Back */
  .card-back {
    background: radial-gradient(ellipse at 40% 45%, var(--indigo-light) 0%, var(--indigo-deep) 75%);
  }
  .world-map {
    position: absolute; left: 90px; top: 70px; width: 520px; height: 270px;
    border-radius: 40% 45% 35% 40%;
    background: radial-gradient(ellipse at center, rgba(140, 150, 220, 0.22) 0%, rgba(140, 150, 220, 0) 70%);
  }
  .feather {
    position: absolute; left: 330px; top: -10px; width: 300px; height: 120px;
    border-radius: 50%;
    transform: rotate(14deg);
    background: radial-gradient(ellipse at 80% 55%, rgba(42, 166, 160, 0.85) 0%, rgba(42, 166, 160, 0.35) 45%, rgba(42, 166, 160, 0) 75%);
  }
  .back-wordmark {
    position: absolute; left: 0; right: 0; top: 170px; text-align: center;
    font-size: 40px; font-weight: 300; letter-spacing: 1px; color: var(--back-text);
  }
</style>
</head>
<body>
  <div class="card card-front">
    <div class="brand">
      <span class="brand-dot"></span>
      <span class="brand-name">Willow Harbor Crafts</span>
    </div>

    <div class="divider"></div>

    <div class="person">
      <div class="person-name">Clara Benton</div>
      <div class="person-role">Director</div>
    </div>

    <ul class="contact-list">
      <li>
        <svg viewBox="0 0 16 16" aria-hidden="true"><path fill="var(--indigo)" d="M4 1l2.5 3-1.5 1.8c.9 2 2.4 3.5 4.2 4.2L11 8.5l3 2.5-1.5 3C7 14 2 9 2 3.5z"/></svg>
        555-318-2047
      </li>
      <li>
        <svg viewBox="0 0 16 16" aria-hidden="true"><rect x="1.5" y="3.5" width="13" height="9" fill="none" stroke="var(--indigo)" stroke-width="1.5"/><path d="M1.5 3.5L8 9l6.5-5.5" fill="none" stroke="var(--indigo)" stroke-width="1.5"/></svg>
        hello@willowharborcrafts.com
      </li>
      <li>
        <svg viewBox="0 0 16 16" aria-hidden="true"><circle cx="8" cy="8" r="6.5" fill="none" stroke="var(--indigo)" stroke-width="1.5"/><ellipse cx="8" cy="8" rx="2.8" ry="6.5" fill="none" stroke="var(--indigo)" stroke-width="1.2"/><path d="M1.5 8h13" stroke="var(--indigo)" stroke-width="1.2"/></svg>
        www.willowharborcrafts.com
      </li>
    </ul>

    <div class="address">Cedar Bluff, TX 75001</div>

    <div class="base-band">
      <div class="band-indigo"></div>
      <div class="band-teal"></div>
    </div>
  </div>

  <div class="card card-back">
    <div class="world-map" role="img" aria-label="Faint dotted world map across the card"></div>
    <div class="feather" role="img" aria-label="Teal peacock feather illustration"></div>
    <div class="back-wordmark">Willow Harbor Crafts</div>
  </div>
</body>
</html>
```